Medical Education and Learning Portal refresh

We at uVeldra Limited have developed a learning platform for medical students. It is based around multiple choice questions, but has social and gaming elements built in to make it fun. It will be used on desktop and mobile devices.

I am looking for a refresh of the 'dated' design into something modern and transferrable between devices.

Note that I have a 'focus group' of Medical Students on 4 February where the Top 3-4 designs will be shown to them for them to pick the winner.

I have also uploaded screenshots of the current site. Essentially I would like to reduce the complexity of design into 2-3 pages (currently unlogged in front/home page, logged in page with options, answer questions page, competition page, revision page/summary pages etc). What I am really after is a good clean colour scheme & structure.

If we get the design colour scheme right then I can pay additionally for coding and maybe some additional structure to pages.
Updates

Target Market(s)

Healthcare/Medical Students

Industry/Entity Type

Healthcare

Number of Pages Required

4 page

Font styles to use
Serif
Sans Serif

Requirements
Must have
• 'Clean' Web 2.0 (or later) feel to it.
• I also expect that the images for the trophies are 'cleaned up (each trophy has a bronze/silver/platinum version as users increase their score. I am looking for these to be clean and simple but fun!
• I also need the final design to be transferrable from a desktop browser to a mobile device. I will need designs for home page/content page/Q&A page.
• I previously had a side panel float over the site but that is dated now and I would like to have a page with each element clearly on it and any information would briefly float over this but not take the focus away from the main function of the page.
• I have included the 'bronze', 'silver', 'gold' trophy icons in the files. These are fine in one sense but ideally the colours will blend well too ...
• The following article summarises my must haves:
• http://pagecraftnotes.example/web-design/web-2-0-design-style-guide/
Nice to have
• Creative concept for presenting MCQ's to students, with a timer and box of information about the question (level of the question, the percent of student who get it right ... etc).
Should not have
• Too much complexity ... clean with a few colours is what I am after
• Note too that my logo is not changing and the colours should blend with this.

```html
<!DOCTYPE html>
<html lang="en">
<head>
<meta charset="utf-8">
<title>uVeldra – Medical Education &amp; Learning Platform</title>
<link href="https://fonts.googleapis.com/css2?family=Ubuntu:wght@400;500;700&family=Open+Sans:wght@400;600;700&display=swap" rel="stylesheet">
<style>
:root{
  --brand-blue:#1570a8;
  --nav-blue:#1474b1;
  --deep-navy:#0e3a55;
  --night:#0b2d44;
  --accent-orange:#f28a1a;
  --ink:#1b3448;
  --body-grey:#555b61;
  --pale:#f5f5f5;
  --line:#d6d9dc;
  --white:#ffffff;
  --band:#2b4a60;
  --band-active:#1f5e86;
  --news-left:#1277b0;
  --news-right:#0f6aa0;
}
*{margin:0;padding:0;box-sizing:border-box}
html,body{width:761px;height:1200px;overflow:hidden}
body{position:relative;background:var(--white);font-family:"Open Sans",Arial,sans-serif;color:var(--body-grey)}
.abs{position:absolute}
.heading{font-family:"Ubuntu",Arial,sans-serif}

/* top strip + header */
.top-strip{left:0;top:0;width:761px;height:4px;background:var(--deep-navy)}
.brand{left:133px;top:12px}
.brand-name{font-family:"Ubuntu",sans-serif;font-size:20px;font-weight:400;color:var(--brand-blue);line-height:22px;letter-spacing:.5px}
.brand-tag{font-size:5.6px;font-weight:700;color:var(--ink);margin-top:3px}
.field{height:14px;border:1px solid #c8ccd0;border-radius:7px;font-size:5.6px;color:#9aa0a6;padding:3px 7px;background:var(--white)}
.btn-pill{height:14px;border-radius:7px;font-size:5.6px;font-weight:700;color:var(--white);text-align:center;line-height:14px;letter-spacing:.4px}
.social{width:14px;height:14px;border-radius:50%;background:#a9adb1}
.social.active{background:var(--brand-blue)}

/* navigation */
.main-nav{left:0;top:55px;width:761px;height:21px;background:var(--nav-blue)}
.nav-item{top:0;height:21px;display:flex;align-items:center;gap:4px;font-size:6.6px;color:var(--white);font-weight:600;font-family:"Open Sans",sans-serif}
.nav-item.current{background:var(--accent-orange);justify-content:center}
.nav-sep{top:0;width:1px;height:21px;background:#2b86bf}

/* hero */
.hero-photo{left:0;top:76px;width:761px;height:178px;background:linear-gradient(100deg,#f2f3f4 0%,#e4e6e8 35%,#b9bdc1 70%,#8d9398 100%)}
.hero-title{left:132px;top:113px;font-size:15px;font-weight:500;color:var(--ink)}
.hero-sub{left:132px;top:130px;font-size:9.6px;color:var(--ink)}
.hero-points{left:132px;top:151px;list-style:none;font-size:7px;color:#2a3a48;line-height:10px}
.hero-points li{display:flex;align-items:center;gap:5px}
.hero-cta{left:132px;top:191px;width:81px;height:19px;border-radius:10px;background:var(--brand-blue);color:var(--white);font-size:7.6px;font-weight:500;text-align:center;line-height:19px;letter-spacing:.3px}

/* features */
.feature-band{left:0;top:254px;width:761px;height:112px;background:linear-gradient(90deg,#2f4c60,#2b4a60 50%,#1f3c52)}
.feature-active{left:253px;top:263px;width:128px;height:94px;background:var(--band-active)}
.feature-divider{left:508px;top:263px;width:1px;height:94px;background:#3d6380}
.feature{top:276px;width:120px;text-align:center}
.feature-title{font-family:"Ubuntu",sans-serif;font-size:10px;color:var(--white);margin-top:6px;letter-spacing:.3px}
.feature-btn{display:inline-block;margin-top:12px;width:49px;height:14px;border-radius:7px;background:var(--brand-blue);color:var(--white);font-size:5.6px;font-weight:700;line-height:14px;letter-spacing:.3px}

/* how it works */
.how-title{left:0;top:397px;width:761px;text-align:center;font-size:15px;font-weight:500;color:#183a55}
.how-sub{left:0;top:415px;width:761px;text-align:center;font-size:7px;color:#222}
.device{background:#e9eaeb;border:1px solid #b9bcbf;border-radius:4px 4px 0 0}
.screen{background:linear-gradient(160deg,#d9d6d2,#8e8a86 55%,#3a3836)}
.device-shadow{left:120px;top:578px;width:520px;height:6px;background:radial-gradient(ellipse at center,rgba(0,0,0,.18),rgba(0,0,0,0) 70%)}

/* about + feed */
.about-left{left:0;top:583px;width:387px;height:269px;background:var(--pale)}
.about-right{left:675px;top:583px;width:86px;height:269px;background:var(--pale)}
.about-title{left:132px;top:620px;font-size:14px;font-weight:500;color:var(--brand-blue);letter-spacing:.4px}
.about-sub{left:132px;top:638px;font-size:7px;color:var(--brand-blue)}
.about-rule{left:119px;top:654px;width:255px;height:1px;background:#c9ccd0}
.about-copy{left:132px;width:229px;font-size:6.5px;line-height:9.1px;color:var(--body-grey)}
.read-more{left:132px;top:802px;font-size:7px;color:var(--brand-blue);display:flex;align-items:center;gap:3px}

.feed{left:430px;top:619px;width:199px;height:197px;border:1px solid var(--line);background:var(--white)}
.feed-head{height:35px;border-bottom:1px solid var(--line);display:flex;align-items:center;justify-content:space-between;padding:0 9px}
.feed-title{font-family:"Ubuntu",sans-serif;font-size:10px;font-weight:700;color:#222}
.follow{border:1px solid #c5c8cb;border-radius:2px;background:#f1f2f3;font-size:5px;font-weight:700;color:#333;padding:1px 4px}
.post{position:relative;height:49px;border-bottom:1px solid #e4e6e8;margin-right:7px;padding:5px 0 0 39px}
.post:last-child{border-bottom:none}
.post-avatar{position:absolute;left:8px;top:9px;width:22px;height:22px;border-radius:3px;background:#2c3338}
.post-name{font-size:6px;font-weight:700;color:#222}
.post-name span{font-weight:400;color:#888;font-size:5px}
.post-date{position:absolute;right:3px;top:5px;font-size:5px;color:#777}
.post-text{font-size:5.6px;line-height:8px;color:#333;margin-top:1px}
.post-text b{font-weight:400;color:var(--brand-blue)}
.post-meta{font-size:5.6px;color:#888;margin-top:2px}
.scrollbar{right:0;top:35px;width:7px;height:161px;border-left:1px solid #e4e6e8;background:#fafafa}

/* newsletter + question */
.news-left{left:0;top:852px;width:387px;height:120px;background:var(--news-left)}
.news-right{left:387px;top:852px;width:374px;height:120px;background:var(--news-right)}
.block-title{font-family:"Ubuntu",sans-serif;font-size:13px;font-weight:500;color:var(--white);letter-spacing:.5px}
.block-text{font-size:7px;line-height:9px;color:#e6f1f8}
.signup{left:132px;top:917px;width:199px;height:14px;border-radius:7px;background:var(--white);overflow:hidden}
.signup-field{position:absolute;left:8px;top:0;font-size:5.8px;color:#8a9096;line-height:14px}
.signup-btn{position:absolute;right:0;top:0;width:71px;height:14px;border-radius:7px;background:var(--deep-navy);color:var(--white);font-size:5.8px;font-weight:700;text-align:center;line-height:14px;letter-spacing:.6px}
.policy{left:133px;top:942px;font-size:6.6px;color:var(--white);text-decoration:underline;display:flex;align-items:center;gap:3px}
.post-btn{left:426px;top:917px;width:63px;height:14px;border-radius:7px;background:var(--accent-orange);color:var(--white);font-size:5.8px;font-weight:700;text-align:center;line-height:14px;letter-spacing:.6px}

/* footer */
.site-footer{left:0;top:972px;width:761px;height:191px;background:var(--deep-navy)}
.footer-divider{left:387px;top:994px;width:1px;height:151px;background:#244f6b}
.footer-head{font-size:7.4px;font-weight:700;color:var(--white);letter-spacing:.3px}
.footer-links{list-style:none;font-size:6.8px;line-height:12.6px;color:#c9d6df}
.footer-links .hot{color:var(--accent-orange)}
.contact{font-size:6.8px;line-height:9.2px;color:#c9d6df}
.contact p{margin-bottom:8.4px}
.bottom-bar{left:0;top:1163px;width:761px;height:37px;background:var(--night)}
.bottom-brand{left:134px;top:1174px;font-family:"Ubuntu",sans-serif;font-size:13px;color:#7f98aa}
.copyright{left:217px;top:1180px;font-size:6.6px;color:#8aa0b0}
.back-top{left:583px;top:1180px;font-size:6.6px;color:#8aa0b0;text-decoration:underline;display:flex;align-items:center;gap:3px}
</style>
</head>
<body>

<div class="abs top-strip"></div>

<!-- header -->
<header>
  <div class="abs brand">
    <div class="brand-name">uVeldra</div>
    <div class="brand-tag">The Medical Peer Review</div>
  </div>
  <div class="abs field" style="left:266px;top:24px;width:101px">Email</div>
  <div class="abs field" style="left:372px;top:24px;width:118px">Password</div>
  <div class="abs btn-pill" style="left:445px;top:24px;width:45px;background:var(--brand-blue)">LOGIN</div>
  <div class="abs btn-pill" style="left:495px;top:24px;width:49px;background:var(--accent-orange)">REGISTER</div>
  <div class="abs social" style="left:563px;top:24px"></div>
  <div class="abs social active" style="left:580px;top:24px"></div>
  <div class="abs social" style="left:597px;top:24px"></div>
  <div class="abs social" style="left:614px;top:24px"></div>
</header>

<!-- navigation -->
<nav class="abs main-nav">
  <div class="abs nav-item current" style="left:132px;width:55px">
    <svg width="9" height="8" viewBox="0 0 9 8"><path d="M4.5 0L0 4h1.2v4h2.4V5.5h1.8V8h2.4V4H9z" fill="#fff"/></svg>Home
  </div>
  <div class="abs nav-sep" style="left:265px"></div>
  <div class="abs nav-item" style="left:199px">
    <svg width="10" height="9" viewBox="0 0 10 9"><rect x=".6" y="2.6" width="8.8" height="5.8" rx="1" fill="none" stroke="#fff" stroke-width="1.1"/><path d="M3 .3l2 2.2 2-2.2" fill="none" stroke="#fff"/></svg>Take the Tour
  </div>
  <div class="abs nav-item" style="left:278px">
    <svg width="17" height="9" viewBox="0 0 17 9"><circle cx="8.5" cy="2.3" r="2.1" fill="#fff"/><path d="M4.5 9c0-3 1.8-4.3 4-4.3s4 1.3 4 4.3z" fill="#fff"/><circle cx="3.3" cy="3.3" r="1.6" fill="#fff"/><path d="M0 9c0-2.3 1.4-3.5 3.3-3.5S6.6 6.7 6.6 9z" fill="#fff"/><circle cx="13.7" cy="3.3" r="1.6" fill="#fff"/><path d="M10.4 9c0-2.3 1.4-3.5 3.3-3.5S17 6.7 17 9z" fill="#fff"/></svg>What Your Peers Say
  </div>
  <div class="abs nav-sep" style="left:381px"></div>
  <div class="abs nav-item" style="left:393px">
    <svg width="9" height="9" viewBox="0 0 10 10"><path d="M5 0l1.5 3.3 3.5.3-2.7 2.4.8 3.5L5 7.7 1.9 9.5l.8-3.5L0 3.6l3.5-.3z" fill="#fff"/></svg>Subscription Plan
  </div>
  <div class="abs nav-sep" style="left:474px"></div>
  <div class="abs nav-item" style="left:486px">
    <svg width="17" height="9" viewBox="0 0 17 9"><circle cx="4.5" cy="2.3" r="2.1" fill="#fff"/><path d="M.5 9c0-3 1.8-4.3 4-4.3s4 1.3 4 4.3z" fill="#fff"/><circle cx="11.5" cy="2.3" r="2.1" fill="#fff"/><path d="M7.5 9c0-3 1.8-4.3 4-4.3s4 1.3 4 4.3z" fill="#fff"/></svg>Friends
  </div>
  <div class="abs nav-sep" style="left:543px"></div>
  <div class="abs nav-item" style="left:555px">
    <svg width="6" height="10" viewBox="0 0 6 10"><rect x=".6" y=".6" width="4.8" height="8.8" rx=".8" fill="none" stroke="#fff" stroke-width="1.1"/><circle cx="3" cy="8" r=".6" fill="#fff"/></svg>Contact Us
  </div>
</nav>

<!-- hero -->
<section>
  <div class="abs hero-photo" role="img" aria-label="Photo of smiling medical professionals looking at a screen in a bright office"></div>
  <h1 class="abs hero-title heading">uVeldra</h1>
  <p class="abs hero-sub heading">Medical Education &amp; Learning Platform</p>
  <ul class="abs hero-points">
    <li><svg width="6" height="6" viewBox="0 0 6 6"><rect x=".4" y=".8" width="4.6" height="4.6" fill="none" stroke="#f28a1a" stroke-width=".8"/><path d="M1.4 2.8l1.3 1.3L5.8.4" fill="none" stroke="#f28a1a" stroke-width="1"/></svg>Know your registered friends progress.</li>
    <li><svg width="6" height="6" viewBox="0 0 6 6"><rect x=".4" y=".8" width="4.6" height="4.6" fill="none" stroke="#f28a1a" stroke-width=".8"/><path d="M1.4 2.8l1.3 1.3L5.8.4" fill="none" stroke="#f28a1a" stroke-width="1"/></svg>Earn trophies with increased knowledge.</li>
    <li><svg width="6" height="6" viewBox="0 0 6 6"><rect x=".4" y=".8" width="4.6" height="4.6" fill="none" stroke="#f28a1a" stroke-width=".8"/><path d="M1.4 2.8l1.3 1.3L5.8.4" fill="none" stroke="#f28a1a" stroke-width="1"/></svg>29.903 Questions answered.</li>
  </ul>
  <div class="abs hero-cta heading">Get Started Now</div>
</section>

<!-- features -->
<section>
  <div class="abs feature-band"></div>
  <div class="abs feature-active"></div>
  <div class="abs feature-divider"></div>
  <div class="abs feature" style="left:129px">
    <svg width="20" height="19" viewBox="0 0 20 19"><circle cx="7" cy="7" r="4.2" fill="none" stroke="#fff" stroke-width="2.6" stroke-dasharray="2 1.3"/><circle cx="14.5" cy="13.5" r="3.2" fill="none" stroke="#fff" stroke-width="2.2" stroke-dasharray="1.6 1.1"/></svg>
    <div class="feature-title">Moderation</div>
    <div class="feature-btn">MORE INFO</div>
  </div>
  <div class="abs feature" style="left:258px">
    <svg width="20" height="19" viewBox="0 0 20 19"><rect x="1" y="13" width="3.5" height="5" fill="#fff"/><rect x="6" y="9" width="3.5" height="9" fill="#fff"/><rect x="11" y="11" width="3.5" height="7" fill="#fff"/><rect x="16" y="2" width="3.5" height="16" fill="#fff"/></svg>
    <div class="feature-title">Statistics</div>
    <div class="feature-btn">MORE INFO</div>
  </div>
  <div class="abs feature" style="left:386px">
    <svg width="20" height="19" viewBox="0 0 20 19"><path d="M5 1h10v6a5 5 0 0 1-10 0z" fill="#fff"/><path d="M5 3H2.5c0 3 1.3 4.5 3 4.8M15 3h2.5c0 3-1.3 4.5-3 4.8" fill="none" stroke="#fff" stroke-width="1.2"/><rect x="9" y="11" width="2" height="4" fill="#fff"/><rect x="6" y="15" width="8" height="3" fill="#fff"/></svg>
    <div class="feature-title">Competition</div>
    <div class="feature-btn">MORE INFO</div>
  </div>
  <div class="abs feature" style="left:514px">
    <svg width="20" height="19" viewBox="0 0 20 19"><path d="M10 1a7 7 0 0 1 7 7c0 3.5-3 5.5-7 10C6 13.5 3 11.5 3 8a7 7 0 0 1 7-7z" fill="#fff"/><text x="10" y="11" font-size="9" font-weight="700" text-anchor="middle" fill="#2b4a60" font-family="Ubuntu,sans-serif">?</text></svg>
    <div class="feature-title">Answer Question</div>
    <div class="feature-btn">MORE INFO</div>
  </div>
</section>

<!-- how it works -->
<section>
  <h2 class="abs how-title heading">How it Work?</h2>
  <p class="abs how-sub">Take a Tour of our Platform now with Video !</p>

  <div class="abs device" style="left:184px;top:495px;width:78px;height:88px;padding:6px 0 0 6px">
    <div class="screen" style="width:72px;height:82px" role="img" aria-label="Video preview of hands playing a piano"></div>
  </div>
  <div class="abs device" style="left:500px;top:495px;width:77px;height:88px;padding:6px 6px 0 0">
    <div class="screen" style="width:71px;height:82px" role="img" aria-label="Video preview of hands playing a piano"></div>
  </div>
  <div class="abs device" style="left:261px;top:441px;width:239px;height:142px;padding:10px 10px 0 10px;border-radius:6px 6px 0 0;background:#f1f1f2">
    <div class="screen" style="width:219px;height:132px" role="img" aria-label="Platform tour video of hands playing a piano"></div>
  </div>
  <div class="abs" style="left:379px;top:446px;width:3px;height:3px;border-radius:50%;background:#333"></div>
  <svg class="abs" style="left:364px;top:502px" width="31" height="31" viewBox="0 0 31 31"><circle cx="15.5" cy="15.5" r="14.5" fill="rgba(255,255,255,.85)"/><path d="M12 9l10 6.5L12 22z" fill="#3a3836"/></svg>
  <svg class="abs" style="left:220px;top:536px" width="16" height="14" viewBox="0 0 16 14"><path d="M15 7H2M7 1L1 7l6 6" fill="none" stroke="#fff" stroke-width="1.6"/></svg>
  <svg class="abs" style="left:529px;top:536px" width="16" height="14" viewBox="0 0 16 14"><path d="M1 7h13M9 1l6 6-6 6" fill="none" stroke="#fff" stroke-width="1.6"/></svg>
  <div class="abs device-shadow"></div>
</section>

<!-- about + feed -->
<section>
  <div class="abs about-left"></div>
  <div class="abs about-right"></div>
  <h2 class="abs about-title heading">uVeldra</h2>
  <p class="abs about-sub">Medical Education and Learning Platform</p>
  <div class="abs about-rule"></div>
  <p class="abs about-copy" style="top:666px">Lorem Ipsum is simply dummy text of the printing and typesetting industry. Lorem Ipsum has been the industry's standard dummy text ever since the 1500s, when an unknown printer took a galley of type and scrambled it to make a type specimen book.</p>
  <p class="abs about-copy" style="top:712px">It is a long established fact that a reader will be distracted by the readable content of a page when looking at its layout. The point of using Lorem Ipsum is that it has a more-or-less normal distribution of letters, as opposed to using 'Content here, content here', making it look like readable English. Many desktop publishing packages and web page editors now use Lorem Ipsum as their default model text, and a search for 'lorem ipsum' will uncover many web sites still in their infancy. Various versions have evolved over the years,...</p>
  <div class="abs read-more"><svg width="6" height="6" viewBox="0 0 6 6"><circle cx="3" cy="3" r="3" fill="#1570a8"/><path d="M1.5 3h3M3 1.6L4.4 3 3 4.4" fill="none" stroke="#fff" stroke-width=".8"/></svg>Read More</div>

  <div class="abs feed">
    <div class="feed-head"><span class="feed-title">Posts</span><span class="follow">Follow</span></div>
    <div class="abs scrollbar"></div>
    <div class="post">
      <div class="post-avatar"></div><span class="post-date">8 Sep</span>
      <div class="post-name">Chirpline <span>@chirpline</span></div>
      <div class="post-text">#fbf to my fav moment building a school in Nepal with strong, humble Tharu women. <b>@schoolraise #nepal #education #women</b></div>
    </div>
    <div class="post">
      <div class="post-avatar"></div><span class="post-date">8 Sep</span>
      <div class="post-name">Chirpline <span>@chirpline</span></div>
      <div class="post-text">#fbf to my fav moment building a school in Nepal with strong, humble Tharu women. <b>@schoolraise #nepal #education #women</b></div>
    </div>
    <div class="post" style="height:62px">
      <div class="post-avatar"></div><span class="post-date">8 Sep</span>
      <div class="post-name">Chirpline <span>@chirpline</span></div>
      <div class="post-text">#fbf to my fav moment building a school in Nepal with strong, humble Tharu women. <b>@schoolraise #nepal #education #women</b></div>
      <div class="post-meta">⇄ Reshared by Chirpline</div>
    </div>
  </div>
</section>

<!-- newsletter + question -->
<section>
  <div class="abs news-left"></div>
  <div class="abs news-right"></div>
  <h3 class="abs block-title" style="left:132px;top:870px">Newsletter</h3>
  <p class="abs block-text" style="left:132px;top:890px;width:215px">Sign up for email and text updates to get deadline reminders and other important information.</p>
  <div class="abs signup"><span class="signup-field">Enter Your Email</span><span class="signup-btn">SIGN UP</span></div>
  <div class="abs policy"><svg width="6" height="6" viewBox="0 0 6 6"><circle cx="3" cy="3" r="3" fill="#fff"/><path d="M1.5 3h3M3 1.6L4.4 3 3 4.4" fill="none" stroke="#1277b0" stroke-width=".8"/></svg>Provacy Policy</div>

  <h3 class="abs block-title" style="left:430px;top:870px;display:flex;align-items:center;gap:4px"><svg width="14" height="14" viewBox="0 0 14 14"><circle cx="7" cy="7" r="7" fill="#fff"/><text x="7" y="10.6" font-size="10" font-weight="700" text-anchor="middle" fill="#0f6aa0" font-family="Ubuntu,sans-serif">?</text></svg>Post Your Question ?</h3>
  <p class="abs block-text" style="left:430px;top:890px;width:180px">Do you have any unique Questions for which looking for Answers?</p>
  <div class="abs post-btn">POST NOW</div>
</section>

<!-- footer -->
<footer>
  <div class="abs site-footer"></div>
  <div class="abs footer-divider"></div>
  <h4 class="abs footer-head" style="left:132px;top:1006px">RESOURCES</h4>
  <ul class="abs footer-links" style="left:132px;top:1022px">
    <li>Take the Tour</li><li class="hot">What your Peers Say</li><li>Subcription Plan</li><li>Friends</li><li>Moderation</li><li>Statistics</li><li>Competition</li><li>Answer Question</li><li>Post Question</li>
  </ul>
  <h4 class="abs footer-head" style="left:259px;top:1006px">QUICK LINK</h4>
  <ul class="abs footer-links" style="left:259px;top:1022px">
    <li>Home</li><li>About</li><li>Contact Us</li><li>Privacy Policy</li><li>T &amp; C's</li><li>Site Map</li>
  </ul>
  <h4 class="abs footer-head" style="left:429px;top:1006px">CONNECT WITH US</h4>
  <div class="abs contact" style="left:429px;top:1024px">
    <p>uVeldra Limited<br>48 Harrow Lane #112 Dunmere, Ma 02190</p>
    <p>Phone<br>+1 555 014 2236</p>
    <p>Email<br>support@uveldralimited.example</p>
  </div>
  <div class="abs social" style="left:429px;top:1109px"></div>
  <div class="abs social" style="left:446px;top:1109px"></div>
  <div class="abs social" style="left:463px;top:1109px"></div>
  <div class="abs social" style="left:480px;top:1109px"></div>

  <div class="abs bottom-bar"></div>
  <div class="abs bottom-brand">uVeldra</div>
  <div class="abs copyright">© 2016 uVeldra Limited . All Rights Reserved</div>
  <div class="abs back-top"><svg width="7" height="7" viewBox="0 0 7 7"><path d="M3.5 7V1M.8 3.5L3.5.8l2.7 2.7" fill="none" stroke="#1570a8" stroke-width="1.4"/></svg>Back to Top</div>
</footer>

</body>
</html>
```